Corporate consulting business needs a business card

I want a professional business card.... surprise me

Updates

Reason: i dont think 2 days is enough

Target Market(s)

Corprorate and Not for Profit firms and organisations

Industry/Entity Type

Consulting

Contact Information for Business Card

Logo
Corporate Consulting Services
On Time, On Budget, Beyond Expectation
Tovan Presfield
Director
0427 31 94 62 (Larger)
tovan@tp-advisory.com.au
www.tp-advisory.com.au
include little icons beside the contact info:

- Envelope = email
- Phone = phone
- Globe = website

Font styles to use
Serif
Sans Serif

Requirements
Must have
• Professional and clean
Nice to have
• you tell me

```html
<!DOCTYPE html>
<html lang="en">
<head>
<meta charset="utf-8">
<title>TP Advisory — Business Cards</title>
<link rel="stylesheet" href="https://fonts.googleapis.com/css2?family=Crimson+Pro:wght@400;600;700&family=Open+Sans:wght@400;600&display=swap">
<style>
  :root {
    --backdrop: #ece7e1;
    --card-white: #ffffff;
    --card-black: #000000;
    --card-brown: #4f2e15;
    --brand-brown: #4a2a14;
    --ink: #111111;
    --ink-soft: #444444;
    --ghost-light: #efefef;
    --ghost-dark: #1e1e1e;
    --white: #ffffff;
    --serif: "Crimson Pro", "Times New Roman", serif;
    --sans: "Open Sans", Arial, sans-serif;
  }
  * { box-sizing: border-box; margin: 0; padding: 0; }
  html, body { width: 1200px; height: 778px; overflow: hidden; }
  body { background: var(--backdrop); position: relative; }

  .card {
    position: absolute;
    width: 530px;
    height: 302px;
    border-radius: 26px;
    overflow: hidden;
    box-shadow: 0 4px 14px rgba(0,0,0,0.18);
  }
  .card--front  { left: 50px;  top: 70px;  background: var(--card-white); }
  .card--black  { left: 620px; top: 70px;  background: var(--card-black); color: var(--white); }
  .card--brown  { left: 50px;  top: 406px; background: var(--card-brown); color: var(--white); }
  .card--light  { left: 620px; top: 406px; background: var(--card-white); color: var(--ink); }

  .ghost-ring {
    position: absolute;
    border-radius: 50%;
    border: 9px solid var(--ghost-light);
  }
  .card--front .ghost-ring { width: 250px; height: 250px; left: 130px; top: 10px; }
  .card--black .ghost-ring { width: 270px; height: 270px; right: -10px; top: 14px; border-color: var(--ghost-dark); }
  .card--light .ghost-ring { width: 190px; height: 190px; right: -10px; top: 80px; }

  .brand {
    position: relative;
    display: flex;
    align-items: center;
    justify-content: center;
    gap: 12px;
    font-family: var(--serif);
    font-weight: 600;
  }
  .brand__dot { border-radius: 50%; border: 5px solid currentColor; }

  .card--front .brand { color: var(--brand-brown); padding-top: 34px; font-size: 44px; }
  .card--front .brand__dot { width: 46px; height: 46px; }
  .card--front .brand-line {
    position: relative; text-align: center; margin-top: 6px;
    font-family: var(--serif); font-weight: 700; font-size: 21px;
    letter-spacing: 0.5px; color: var(--ink); text-transform: uppercase;
  }
  .holder {
    position: relative; text-align: center; margin-top: 14px;
    font-family: var(--serif); font-size: 23px; color: var(--brand-brown);
  }
  .holder__role { font-size: 18px; color: var(--ink-soft); }
  .contact {
    position: relative; display: flex; align-items: center; justify-content: center;
    gap: 8px; font-family: var(--serif); color: var(--ink);
  }
  .contact svg { width: 14px; height: 14px; fill: none; stroke: currentColor; stroke-width: 1.6; }
  .contact--phone { font-size: 20px; margin-top: 8px; }
  .contact--email { font-size: 17px; margin-top: 2px; color: var(--ink-soft); }
  .web-band {
    position: absolute; left: 0; right: 0; bottom: 0; height: 44px;
    background: var(--card-black); color: var(--white);
    display: flex; align-items: center; justify-content: center; gap: 10px;
    font-family: var(--serif); font-size: 19px;
  }
  .web-band svg { width: 15px; height: 15px; fill: none; stroke: currentColor; stroke-width: 1.4; }

  .tagline { position: relative; font-family: var(--sans); }
  .card--black .tagline, .card--light .tagline { padding: 44px 0 0 30px; }
  .tagline__title { font-size: 19px; }
  .card--light .tagline__title { font-size: 20px; }
  .tagline__list { list-style: none; margin-top: 14px; font-size: 13.5px; }
  .card--light .tagline__list { font-size: 14.5px; }
  .tagline__list li { display: flex; align-items: center; gap: 8px; margin-bottom: 6px; }
  .tagline__list li::before {
    content: ""; width: 5px; height: 5px; border-radius: 50%; background: currentColor;
  }
  .site {
    position: absolute; left: 30px; bottom: 36px;
    font-family: var(--sans); font-size: 14px; letter-spacing: 0.3px;
  }

  .card--brown .brand { padding-top: 44px; font-size: 50px; color: var(--white); }
  .card--brown .brand__dot { width: 52px; height: 52px; }
  .card--brown .tagline { text-align: center; margin-top: 34px; }
  .card--brown .tagline__list {
    display: flex; justify-content: center; gap: 14px; margin-top: 8px; font-size: 14.5px;
  }
  .card--brown .tagline__list li { margin: 0; }
  .card--brown .site { left: 0; right: 0; bottom: 38px; text-align: center; }
</style>
</head>
<body>

<section class="card card--front" aria-label="Card front with contact details">
  <div class="ghost-ring"></div>
  <div class="brand"><span class="brand__dot"></span>TP Advisory</div>
  <div class="brand-line">Consulting Services</div>
  <p class="holder">Tovan Presfield, <span class="holder__role">Director</span></p>
  <p class="contact contact--phone">
    <svg viewBox="0 0 14 14"><rect x="4" y="1" width="6" height="12" rx="1"/><line x1="6" y1="11" x2="8" y2="11"/></svg>
    0427 31 94 62
  </p>
  <p class="contact contact--email">
    <svg viewBox="0 0 14 14"><rect x="1" y="3" width="12" height="8" rx="1"/><polyline points="1,3 7,8 13,3"/></svg>
    tovan@tp-advisory.com.au
  </p>
  <div class="web-band">
    <svg viewBox="0 0 16 16"><circle cx="8" cy="8" r="6.5"/><ellipse cx="8" cy="8" rx="3" ry="6.5"/><line x1="1.5" y1="8" x2="14.5" y2="8"/></svg>
    www.tp-advisory.com.au
  </div>
</section>

<section class="card card--black" aria-label="Card back, black">
  <div class="ghost-ring"></div>
  <div class="tagline">
    <p class="tagline__title">Corporate Consulting Services</p>
    <ul class="tagline__list"><li>On Time</li><li>On Budget</li><li>Beyond Expectation</li></ul>
  </div>
  <p class="site">www.tp-advisory.com.au</p>
</section>

<section class="card card--brown" aria-label="Card back, brown">
  <div class="brand"><span class="brand__dot"></span>TP Advisory</div>
  <div class="tagline">
    <p class="tagline__title">Corporate Consulting Services</p>
    <ul class="tagline__list"><li>On Time</li><li>On Budget</li><li>Beyond Expectation</li></ul>
  </div>
  <p class="site">www.tp-advisory.com.au</p>
</section>

<section class="card card--light" aria-label="Card back, white">
  <div class="ghost-ring"></div>
  <div class="tagline">
    <p class="tagline__title">Corporate Consulting Services</p>
    <ul class="tagline__list"><li>On Time</li><li>On Budget</li><li>Beyond Expectation</li></ul>
  </div>
  <p class="site">www.tp-advisory.com.au</p>
</section>

</body>
</html>
```